Corvanel Business card

I got my logo so I need to have that on my business card!!

Thanks
Updates

Reason: Hi designers, i will be deciding my logo by this weekend!!! As soon as I decide i will post my logo for your application Thanks Fedorico

I Just sent my logo for your attention!!!

Target Market(s)

My costumers will be enginners from shipyard industry!

Industry/Entity Type

Business

Requirements
Must have
• My future logo

```html
<!DOCTYPE html>
<html lang="en">
<head>
<meta charset="utf-8">
<title>Corvanel Business Card</title>
<link href="https://fonts.googleapis.com/css2?family=Oswald:wght@500&family=Open+Sans:wght@300;400;700&display=swap" rel="stylesheet">
<style>
  :root {
    --orange: #f0a347;
    --orange-soft: #f6c88f;
    --white: #ffffff;
    --ink: #222222;
    --backdrop: #e4e4e4;
  }
  * { box-sizing: border-box; margin: 0; padding: 0; }
  html, body { width: 1200px; height: 600px; overflow: hidden; }
  body {
    background: var(--backdrop);
    font-family: "Open Sans", Arial, sans-serif;
    position: relative;
  }
  .card {
    position: absolute;
    top: 147px;
    width: 448px;
    height: 260px;
    overflow: hidden;
  }
  .card-front { left: 119px; background: var(--white); }
  .card-back { left: 637px; background: var(--orange); }

  .holder-name {
    position: absolute; left: 58px; top: 58px;
    font-family: "Oswald", "Arial Narrow", sans-serif;
    font-weight: 500; font-size: 17px; color: var(--orange);
    letter-spacing: 0.3px;
  }
  .holder-role {
    position: absolute; left: 90px; top: 82px;
    font-size: 10.5px; color: var(--ink); letter-spacing: 0.3px;
  }
  .contact-list { position: absolute; left: 53px; top: 148px; list-style: none; }
  .contact-list li {
    display: flex; align-items: center; gap: 5px;
    font-size: 9.5px; color: var(--ink); height: 16px;
  }
  .contact-list li.gap-after { margin-bottom: 6px; }
  .contact-list svg { width: 10px; height: 10px; fill: var(--orange); }

  .arm-decoration {
    position: absolute; left: 187px; top: 17px;
    width: 240px; height: 195px;
    background: linear-gradient(160deg, var(--orange-soft), var(--orange));
    border-radius: 6px 6px 0 0;
  }

  .tagline-band {
    position: absolute; left: 0; bottom: 0; width: 100%; height: 48px;
    background: var(--orange);
    display: flex; align-items: center; padding-left: 50px; gap: 18px;
  }
  .tagline-band svg { width: 10px; height: 10px; fill: var(--white); }
  .tagline {
    color: var(--white); font-weight: 700; font-size: 10px; letter-spacing: 0.4px;
  }

  .brand-block {
    position: absolute; left: 0; right: 0; top: 62px;
    display: flex; flex-direction: column; align-items: center;
  }
  .brand-dot {
    width: 44px; height: 44px; border-radius: 50%; background: var(--white);
    margin-bottom: 14px;
  }
  .brand-name {
    font-weight: 300; font-size: 44px; color: var(--white); line-height: 1;
  }
  .brand-web {
    margin-top: 16px; font-weight: 700; font-size: 10px; color: var(--white);
  }
</style>
</head>
<body>
  <section class="card card-front">
    <h1 class="holder-name">NAME NAME</h1>
    <p class="holder-role">REALTOR</p>
    <ul class="contact-list">
      <li class="gap-after">
        <svg viewBox="0 0 10 10"><path d="M2 1h2l1 2.5-1.2 1a5 5 0 0 0 2.7 2.7l1-1.2L10 7v2a1 1 0 0 1-1 1A8 8 0 0 1 1 2a1 1 0 0 1 1-1z"/></svg>
        555 204 7183
      </li>
      <li>
        <svg viewBox="0 0 10 10"><path d="M0 2h10v6H0z M0 2l5 3.5L10 2" stroke="#fff" stroke-width="0.8"/></svg>
        info@corvanel.com
      </li>
      <li>
        <svg viewBox="0 0 10 10"><path d="M0 1h10v6H0zM1 2v4h8V2zM3 8h4v1H3z"/></svg>
        www.corvanel.com
      </li>
    </ul>
    <div class="arm-decoration" role="img" aria-label="Large decorative brand illustration area"></div>
    <div class="tagline-band">
      <svg viewBox="0 0 10 10"><path d="M5 0l5 5H8.5v5h-2.5V7H4v3H1.5V5H0z"/></svg>
      <p class="tagline">LOREM IPSUM IS SIMPLY DUMMY TEXT OF THE PRINTING</p>
    </div>
  </section>

  <section class="card card-back">
    <div class="brand-block">
      <span class="brand-dot"></span>
      <p class="brand-name">Corvanel</p>
      <p class="brand-web">www.corvanel.com</p>
    </div>
  </section>
</body>
</html>
```